Quorvilan Mobile App

We are in need of a design for a mobile application that delivers relevant content to users based on the profile that they enter and based on the answers that they enter in a daily health tracker. There also will be functionality that will allow a user to check the cost of a medical service/ procedure before going to the medical provider (could get a list of providers and costs after entering procedure, service or prescription in a search box). The content will be articles or information that our team will find/develop on a daily basis and put into a database that the app will pull off of. The profile needs to capture age, sex, ethinicity (optional) and then have a list of topics that the user can select to get daily updated information/content. These topics are: Diabetes, Heart Disease, Hypertension, COPD, Back Pain, Weight Management, Depression, Cancer, Wellness Plan. The final design should allow for users to receive helpful health care information every day based on their profile and the answers in the daily health tracker.

Medical

```html
<!DOCTYPE html>
<html lang="en">
<head>
<meta charset="utf-8">
<title>Quorvilan Health Tracker</title>
<link href="https://fonts.googleapis.com/css2?family=Arimo:wght@400;700&display=swap" rel="stylesheet">
<style>
  :root {
    --bg: #eeeeee;
    --screen: #ffffff;
    --status-top: #3a3a3a;
    --status-bottom: #151515;
    --status-text: #e8e8e8;
    --nav-top: #ffffff;
    --nav-bottom: #e4e4e4;
    --green: #3dbf1e;
    --green-dark: #259a0e;
    --green-text: #45c22a;
    --blue: #1b5f98;
    --ink: #3a3a3a;
    --muted: #9a9a9a;
    --ring: #bdbdbd;
    --field: #ebebeb;
    --rule: #dcdcdc;
  }
  * { box-sizing: border-box; margin: 0; padding: 0; }
  html, body {
    width: 1200px; height: 2364px; overflow: hidden;
    background: var(--bg);
    font-family: "Arimo", Arial, sans-serif;
  }
  .screen {
    position: absolute; left: 0; top: 282px;
    width: 640px; height: 960px;
    transform: scale(1.875); transform-origin: 0 0;
    background: var(--screen);
    overflow: hidden;
  }
  .abs { position: absolute; }

  .status-bar {
    left: 0; top: 0; width: 640px; height: 40px;
    background: linear-gradient(var(--status-top), var(--status-bottom));
    color: var(--status-text); font-weight: 700; font-size: 24px;
  }
  .status-bar .carrier { left: 8px; top: 6px; display: flex; align-items: center; gap: 6px; }
  .status-bar .dots { font-size: 14px; letter-spacing: 1px; margin-top: 6px; }
  .status-bar .time { left: 0; width: 640px; text-align: center; top: 6px; }
  .status-bar .battery { right: 8px; top: 6px; display: flex; align-items: center; gap: 6px; }

  .nav-bar {
    left: 0; top: 40px; width: 640px; height: 77px;
    background: linear-gradient(var(--nav-top), var(--nav-bottom));
    border-bottom: 1px solid #cfcfcf;
  }
  .nav-bar .back-label { left: 17px; top: 24px; font-size: 30px; color: var(--green); }
  .nav-bar .title { left: 0; width: 660px; text-align: center; top: 23px; font-size: 32px; color: var(--blue); }
  .nav-bar .add { left: 576px; top: 20px; }

  .search-row { left: 0; top: 117px; width: 640px; height: 76px; border-bottom: 1px solid var(--rule); }
  .search-row .icon { left: 26px; top: 22px; }
  .search-row .label { left: 62px; top: 22px; font-size: 26px; color: var(--muted); }
  .search-row .field {
    left: 170px; top: 16px; width: 432px; height: 46px;
    border: 2px solid var(--green); border-radius: 8px; background: var(--field);
  }

  .intro { left: 64px; top: 220px; width: 540px; font-size: 19px; line-height: 25px; color: var(--green-text); }

  .question { left: 68px; font-size: 21px; line-height: 27px; color: var(--ink); width: 540px; }
  .option { display: flex; align-items: center; gap: 11px; font-size: 17px; color: var(--muted); height: 30px; }
  .radio { width: 29px; height: 29px; border-radius: 50%; border: 1.5px solid var(--ring); background: #fff; flex: none; }
  .radio.checked { border: none; background: var(--green); display: flex; align-items: center; justify-content: center; }

  .hint { left: 68px; top: 816px; font-size: 17px; color: var(--green-text); }
  .result-field { left: 299px; top: 810px; width: 216px; height: 34px; border: 1.5px solid #d0d0d0; border-radius: 6px; background: var(--field); }

  .submit {
    left: 224px; top: 880px; width: 172px; height: 46px;
    border: 1.5px solid var(--green-dark); border-radius: 6px;
    background: linear-gradient(#55d232, #2ea812);
    color: #fff; font-weight: 700; font-size: 20px;
    display: flex; align-items: center; justify-content: center;
  }
</style>
</head>
<body>
<main class="screen">
  <header class="abs status-bar">
    <div class="abs carrier"><span class="dots">▪▫▫▫▫</span>Nettra
      <svg width="28" height="20" viewBox="0 0 28 20"><path d="M2 7a17 17 0 0 1 24 0M6 11a11 11 0 0 1 16 0M10 15a5 5 0 0 1 8 0" fill="none" stroke="#e8e8e8" stroke-width="3" stroke-linecap="round"/></svg>
    </div>
    <div class="abs time">19:37</div>
    <div class="abs battery">64%
      <svg width="38" height="20" viewBox="0 0 38 20"><rect x="1" y="2" width="32" height="16" rx="3" fill="none" stroke="#e8e8e8" stroke-width="2"/><rect x="4" y="5" width="17" height="10" fill="#e8e8e8"/><rect x="34" y="7" width="3" height="6" fill="#e8e8e8"/></svg>
    </div>
  </header>

  <nav class="abs nav-bar">
    <div class="abs back-label">Label</div>
    <div class="abs title">Health Tracker</div>
    <svg class="abs add" width="34" height="34" viewBox="0 0 34 34"><path d="M17 2v30M2 17h30" stroke="#3dbf1e" stroke-width="2.5"/></svg>
  </nav>

  <section class="abs search-row">
    <svg class="abs icon" width="28" height="28" viewBox="0 0 28 28"><circle cx="11" cy="11" r="8" fill="none" stroke="#3dbf1e" stroke-width="2.2"/><path d="M17 17l8 8" stroke="#3dbf1e" stroke-width="2.5" stroke-linecap="round"/></svg>
    <div class="abs label">Search</div>
    <div class="abs field"></div>
  </section>

  <p class="abs intro">This is your personal health tracker…keep a record of your healthy behaviors and access the history anytime</p>

  <div class="abs question" style="top:300px">How many hours did you sleep last night?</div>
  <div class="abs option" style="left:68px;top:328px"><span class="radio"></span>Less than 6 hours</div>
  <div class="abs option" style="left:285px;top:328px"><span class="radio checked"><svg width="16" height="12" viewBox="0 0 16 12"><path d="M1.5 6l4.5 4.5L14.5 1.5" fill="none" stroke="#fff" stroke-width="2.2"/></svg></span>More than 6 hours</div>

  <div class="abs question" style="top:371px">Have you exercised today?</div>
  <div class="abs option" style="left:68px;top:400px"><span class="radio"></span>Yes</div>
  <div class="abs option" style="left:176px;top:400px"><span class="radio checked"><svg width="16" height="12" viewBox="0 0 16 12"><path d="M1.5 6l4.5 4.5L14.5 1.5" fill="none" stroke="#fff" stroke-width="2.2"/></svg></span>No</div>

  <div class="abs question" style="top:441px">Have you had a cigarette today?</div>
  <div class="abs option" style="left:68px;top:471px"><span class="radio"></span>Yes</div>
  <div class="abs option" style="left:176px;top:471px"><span class="radio checked"><svg width="16" height="12" viewBox="0 0 16 12"><path d="M1.5 6l4.5 4.5L14.5 1.5" fill="none" stroke="#fff" stroke-width="2.2"/></svg></span>No</div>

  <div class="abs question" style="top:512px">Have you had any alcoholic beverages today?</div>
  <div class="abs option" style="left:68px;top:541px"><span class="radio"></span>Yes</div>
  <div class="abs option" style="left:176px;top:541px"><span class="radio checked"><svg width="16" height="12" viewBox="0 0 16 12"><path d="M1.5 6l4.5 4.5L14.5 1.5" fill="none" stroke="#fff" stroke-width="2.2"/></svg></span>No</div>

  <div class="abs question" style="top:583px">How would you describe your eating over the last 24 hours?</div>
  <div class="abs option" style="left:68px;top:639px"><span class="radio"></span>Healthy</div>
  <div class="abs option" style="left:197px;top:639px"><span class="radio"></span>Not bad</div>
  <div class="abs option" style="left:331px;top:639px"><span class="radio checked"><svg width="16" height="12" viewBox="0 0 16 12"><path d="M1.5 6l4.5 4.5L14.5 1.5" fill="none" stroke="#fff" stroke-width="2.2"/></svg></span>Needs Improvement</div>

  <div class="abs question" style="top:680px">How would you describe your stress level over the last 24 hours?</div>
  <div class="abs option" style="left:68px;top:737px"><span class="radio"></span>Low/None</div>
  <div class="abs option" style="left:226px;top:737px"><span class="radio"></span>Slightly Elevated</div>
  <div class="abs option" style="left:439px;top:737px"><span class="radio checked"><svg width="16" height="12" viewBox="0 0 16 12"><path d="M1.5 6l4.5 4.5L14.5 1.5" fill="none" stroke="#fff" stroke-width="2.2"/></svg></span>High</div>

  <div class="abs question" style="top:779px">Have you checked your insulin levels today?</div>
  <div class="abs hint">If yes, enter results here:</div>
  <div class="abs result-field"></div>

  <div class="abs submit">SUBMIT</div>
</main>
</body>
</html>
```